Meridian Handsets business card design

I would like to see some designs for a business card for Meridian Handsets. I would like the business card to be double sided. It will need to have a similar colour / look and feel to our website www.meridianhandsets.com.au I have also attached our latest flyer. Final designs to be handed over in Photoshop format so that I can edit the business card when needed please.

Industry/Entity Type

Business

Contact Information for Business Card

Gavin Thornley
sales@meridianhandsets.com.au
Business Development Manager
ph: (08) 6197 5821
www.meridianhandsets.com.au

Font styles to use
Serif
Sans Serif

Requirements
Must have
• If you could please utilise our colour scheme as seen on our website and the attached flyer.
• I would also like the final design to be in a Photoshop format so that I can edit it when needed please.

```html
<!DOCTYPE html>
<html lang="en">
<head>
<meta charset="utf-8">
<title>Meridian Handsets – Business Card</title>
<link href="https://fonts.googleapis.com/css2?family=Open+Sans:wght@400;600;700&display=swap" rel="stylesheet">
<style>
  :root {
    --page-bg: #e9eaec;
    --card-dark: #343434;
    --ink: #2b2b2b;
    --brand-blue: #1a7fc1;
    --white: #ffffff;
    --card-w: 600px;
    --card-h: 367px;
  }
  * { box-sizing: border-box; margin: 0; padding: 0; }
  html, body {
    width: 1200px; height: 900px; overflow: hidden;
    background: var(--page-bg);
    font-family: "Open Sans", Arial, sans-serif;
  }
  .sheet {
    width: 1200px; height: 900px;
    display: flex; flex-direction: column;
    align-items: center; justify-content: center; gap: 50px;
  }
  .card {
    position: relative;
    width: var(--card-w); height: var(--card-h);
    overflow: hidden;
    box-shadow: 0 8px 24px rgba(0,0,0,.18);
  }
  /* Back side */
  .card-back {
    background: var(--card-dark);
    display: flex; align-items: center; justify-content: center;
  }
  .back-url {
    color: var(--white);
    font-size: 20px; letter-spacing: 1px;
  }
  .back-url .domain { color: var(--brand-blue); }

  /* Front side */
  .card-front { background: var(--white); }
  .front-shape { position: absolute; inset: 0; }
  .identity {
    position: absolute; left: 34px; top: 92px;
  }
  .brand-name {
    color: var(--ink);
    font-size: 38px; font-weight: 600;
    letter-spacing: -0.5px; line-height: 1;
  }
  .person-name {
    margin-top: 14px;
    color: var(--ink);
    font-size: 22px; font-weight: 700; letter-spacing: 2px;
  }
  .person-title {
    margin-top: 2px;
    color: var(--brand-blue);
    font-size: 14px; letter-spacing: 1px;
  }
  .contact-list {
    position: absolute; right: 26px; bottom: 46px;
    list-style: none; color: var(--white);
    font-size: 13px; line-height: 1.35; text-align: right;
  }
  .contact-list li {
    display: flex; align-items: center; justify-content: flex-end; gap: 8px;
  }
  .contact-icon { width: 11px; height: 11px; flex: none; }
</style>
</head>
<body>
<main class="sheet">
  <section class="card card-back" aria-label="Business card back">
    <p class="back-url">www.<span class="domain">meridianhandsets.com.au</span></p>
  </section>

  <section class="card card-front" aria-label="Business card front">
    <svg class="front-shape" viewBox="0 0 600 367" preserveAspectRatio="none" aria-hidden="true">
      <path d="M402 0 H600 V367 H222 C338 298 402 168 402 0 Z" fill="#343434"/>
      <path d="M418 0 H600 V367 H246 C356 298 418 168 418 0 Z" fill="#1a7fc1"/>
    </svg>

    <div class="identity">
      <h1 class="brand-name">Meridian Handsets</h1>
      <h2 class="person-name">Gavin Thornley</h2>
      <p class="person-title">Business Development Manager</p>
    </div>

    <ul class="contact-list">
      <li>(08) 6197 5821
        <svg class="contact-icon" viewBox="0 0 24 24" aria-hidden="true"><path fill="#343434" d="M6.6 10.8a15.1 15.1 0 0 0 6.6 6.6l2.2-2.2c.3-.3.7-.4 1-.2 1.1.4 2.3.6 3.6.6.6 0 1 .4 1 1V20c0 .6-.4 1-1 1A17 17 0 0 1 3 4c0-.6.4-1 1-1h3.5c.6 0 1 .4 1 1 0 1.3.2 2.5.6 3.6.1.3 0 .7-.2 1z"/></svg>
      </li>
      <li>sales@meridianhandsets.com.au
        <svg class="contact-icon" viewBox="0 0 24 24" aria-hidden="true"><rect x="2" y="5" width="20" height="14" rx="1" fill="none" stroke="#343434" stroke-width="2"/><path d="M2 6l10 7 10-7" fill="none" stroke="#343434" stroke-width="2"/></svg>
      </li>
      <li>www.meridianhandsets.com.au
        <svg class="contact-icon" viewBox="0 0 24 24" aria-hidden="true"><circle cx="12" cy="12" r="10" fill="none" stroke="#343434" stroke-width="2"/><path d="M2 12h20M12 2c3 3 3 17 0 20M12 2c-3 3-3 17 0 20" fill="none" stroke="#343434" stroke-width="2"/></svg>
      </li>
    </ul>
  </section>
</main>
</body>
</html>
```